New Business Card Design Project

We require a business card design for Zelvaquin, a newly established Indian company.
Our focus is on the development, manufacturing, and export of a diverse array of pharmaceutical products on a global scale. The card should convey a professional appearance, as our primary markets are in Africa, China, and Southeast Asian nations.
We envision a two-sided business card, with the reverse side dedicated to a logo set against a solid color or an elegantly designed pattern. The corners should be rounded. We would appreciate seeing both horizontal and vertical design options. We trust the designer to utilize their expertise in creating this design.

The content for the business card is included in the attached Word file.

Target Market(s)

Our primary markets are in Africa, China, and Southeast Asian, Latin America, Maldives, Sri Lanka

Industry/Entity Type

Pharmaceutical Manufacturing and Export

Contact Information for Business Card

Colors

Designer to choose colors to be used in the design.

Requirements
Must have
• The reverse side of the business card features solely the logo along with the tagline, "Care Beyond Borders."
Should not have
• The logo should not exceed two instances, encompassing both the front and back sides of the card.

```html
<!DOCTYPE html>
<html lang="en">
<head>
<meta charset="utf-8">
<title>Zelvaquin Business Card</title>
<link rel="stylesheet" href="https://fonts.googleapis.com/css2?family=Montserrat:wght@500;600;700&family=Lato:wght@400&display=swap">
<style>
  :root {
    --backdrop: #1b1b1d;
    --card: #262628;
    --blue: #2aa6e0;
    --coral: #f1604c;
    --white: #f4f4f4;
    --muted: #c9c9cc;
  }
  html, body {
    margin: 0;
    width: 1200px;
    height: 952px;
    overflow: hidden;
    background: var(--backdrop);
  }
  .canvas {
    position: relative;
    width: 1200px;
    height: 952px;
  }
  .card {
    position: absolute;
    width: 560px;
    height: 320px;
    background: var(--card);
    border-radius: 14px;
    overflow: hidden;
    box-shadow: 0 18px 40px rgba(0,0,0,.45);
  }
  .card--front { left: 580px; top: 110px; }
  .card--back  { left: 60px;  top: 520px; }

  /* front side */
  .holder {
    position: absolute;
    left: 44px;
    top: 38px;
  }
  .holder__name {
    margin: 0;
    font: 600 26px/1 "Montserrat", sans-serif;
    letter-spacing: .5px;
    color: var(--blue);
  }
  .holder__name .surname { color: var(--coral); }
  .holder__role {
    margin: 8px 0 0;
    font: 500 17px/1 "Montserrat", sans-serif;
    color: var(--white);
  }
  .address {
    position: absolute;
    left: 44px;
    top: 120px;
    display: flex;
    gap: 10px;
    font: 400 13px/1.35 "Lato", sans-serif;
    color: var(--white);
  }
  .contact-band {
    position: absolute;
    left: 0;
    top: 172px;
    width: 330px;
    height: 100px;
    background: var(--coral);
    clip-path: polygon(0 0, 100% 0, 78% 100%, 0 100%);
  }
  .contact-list {
    list-style: none;
    margin: 0;
    padding: 14px 0 0 44px;
    display: grid;
    gap: 7px;
    font: 400 14px/1 "Lato", sans-serif;
    color: var(--white);
  }
  .contact-list li { display: flex; align-items: center; gap: 10px; }
  .icon {
    width: 17px;
    height: 17px;
    border-radius: 3px;
    background: var(--blue);
    display: inline-flex;
    align-items: center;
    justify-content: center;
    flex: none;
  }
  .icon svg { width: 11px; height: 11px; fill: var(--white); }

  /* back side */
  .brand {
    position: absolute;
    left: 0; right: 0; top: 104px;
    text-align: center;
  }
  .brand__name {
    display: inline-flex;
    align-items: center;
    gap: 12px;
    margin: 0;
    font: 700 50px/1 "Montserrat", sans-serif;
    color: var(--blue);
  }
  .brand__dot {
    width: 20px;
    height: 20px;
    border-radius: 50%;
    background: var(--coral);
  }
  .brand__tagline {
    margin: 14px 0 0;
    font: 400 16px/1 "Lato", sans-serif;
    letter-spacing: 3px;
    text-transform: uppercase;
    color: var(--muted);
  }
</style>
</head>
<body>
<main class="canvas">
  <section class="card card--front" aria-label="Card front">
    <div class="holder">
      <h1 class="holder__name">ROHAN K. <span class="surname">DESHMANE</span></h1>
      <p class="holder__role">CEO/Zelvaquin</p>
    </div>
    <div class="address">
      <span class="icon"><svg viewBox="0 0 12 12"><path d="M6 0a4 4 0 0 0-4 4c0 3 4 8 4 8s4-5 4-8a4 4 0 0 0-4-4zm0 5.6A1.6 1.6 0 1 1 6 2.4a1.6 1.6 0 0 1 0 3.2z"/></svg></span>
      <span>12, Suvarna Nagar, Nashik,<br>422005, India</span>
    </div>
    <div class="contact-band">
      <ul class="contact-list">
        <li><span class="icon"><svg viewBox="0 0 12 12"><path d="M2.4 0 4.3 2.3 3.2 3.8a7 7 0 0 0 5 5l1.5-1.1L12 9.6 10.6 12C5 12 0 7 0 1.4z"/></svg></span>+919812345670</li>
        <li><span class="icon"><svg viewBox="0 0 12 12"><path d="M0 2h12v1L6 7 0 3zm0 2.4 6 4 6-4V10H0z"/></svg></span>rdeshmane@zelvaquin.com</li>
        <li><span class="icon"><svg viewBox="0 0 12 12"><path d="M6 0 11 11 6 8 1 11z"/></svg></span>rdeshmane@zelvaquin.com</li>
      </ul>
    </div>
  </section>

  <section class="card card--back" aria-label="Card back">
    <div class="brand">
      <p class="brand__name">Zelvaquin<span class="brand__dot"></span></p>
      <p class="brand__tagline">Care Beyond Borders</p>
    </div>
  </section>
</main>
</body>
</html>
```